Fenwick Business Card Design

Photography business needs a logo. I would like to see creative licence on options on 1 & 2 sided. I really like the concept of a fully / partially frosted design. I have already used SketchHarbor for my Logo, so I am looking for the same level of assistance with this project.

Industry/Entity Type

Business

Font styles to use
Serif
Script

Requirements
Must have
• Must Have:
• - These are my contact details
• Name: Paul K Fenwick
• Mobile: 5183402917
• email: lisamerrow@quillpost.com

```html
<!DOCTYPE html>
<html lang="en">
<head>
<meta charset="utf-8">
<title>Fenwick Business Card Design</title>
<link rel="stylesheet" href="https://fonts.googleapis.com/css2?family=Arimo:wght@400;700&display=swap">
<style>
  :root {
    --backdrop: #e9e7e4;
    --card-black: #000000;
    --card-grey-light: #f2f2f2;
    --card-grey: #c9c9c9;
    --accent-blue: #0ea2d1;
    --paper-white: #ffffff;
    --ink: #111111;
    --ink-soft: #555555;
    --shadow: rgba(0, 0, 0, 0.25);
  }
  * { box-sizing: border-box; margin: 0; padding: 0; }
  html, body {
    width: 1200px;
    height: 918px;
    overflow: hidden;
    background: var(--backdrop);
    font-family: "Arimo", Arial, sans-serif;
  }
  .canvas {
    position: relative;
    width: 1200px;
    height: 918px;
  }
  .card {
    position: absolute;
    width: 540px;
    height: 310px;
    overflow: hidden;
    box-shadow: 0 10px 24px var(--shadow);
  }

  /* Front card: frosted grey */
  .card--front {
    left: 600px;
    top: 120px;
    background: radial-gradient(ellipse at 40% 45%, var(--card-grey-light) 0%, #dedede 40%, var(--card-grey) 100%);
  }
  .front__band {
    position: absolute;
    left: 210px;
    top: 34px;
    width: 300px;
    height: 16px;
    background: var(--accent-blue);
  }
  .front__corner-block {
    position: absolute;
    left: 470px;
    top: 50px;
    width: 70px;
    height: 20px;
    background: var(--paper-white);
  }
  .front__side-blue {
    position: absolute;
    left: 0;
    top: 150px;
    width: 36px;
    height: 60px;
    background: var(--accent-blue);
  }
  .front__side-white {
    position: absolute;
    left: 0;
    top: 176px;
    width: 60px;
    height: 64px;
    background: var(--paper-white);
  }
  .front__ghost-name {
    position: absolute;
    left: 110px;
    top: 78px;
    font-size: 120px;
    font-weight: 700;
    letter-spacing: -2px;
    color: var(--paper-white);
    opacity: 0.55;
    line-height: 1;
  }
  .front__name {
    position: absolute;
    left: 28px;
    top: 78px;
    font-size: 30px;
    font-weight: 700;
    letter-spacing: -0.5px;
    color: var(--ink);
    line-height: 1;
  }
  .front__role {
    position: absolute;
    left: 102px;
    top: 112px;
    font-size: 13px;
    color: var(--ink-soft);
    letter-spacing: 0.5px;
  }
  .front__contact {
    position: absolute;
    right: 36px;
    bottom: 30px;
    font-size: 11px;
    color: var(--ink-soft);
    line-height: 1.5;
  }
  .front__contact dt { display: inline; }
  .front__contact dd { display: inline; margin-left: 4px; }

  /* Back card: black */
  .card--back {
    left: 60px;
    top: 470px;
    background: var(--card-black);
  }
  .back__corner-block {
    position: absolute;
    left: 0;
    top: 0;
    width: 70px;
    height: 30px;
    background: var(--paper-white);
  }
  .back__band {
    position: absolute;
    left: 70px;
    top: 0;
    width: 440px;
    height: 22px;
    background: var(--accent-blue);
  }
  .back__band-thin {
    position: absolute;
    left: 70px;
    top: 26px;
    width: 440px;
    height: 6px;
    background: var(--accent-blue);
  }
  .back__name {
    position: absolute;
    left: 36px;
    top: 118px;
    font-size: 56px;
    font-weight: 400;
    color: var(--paper-white);
    line-height: 1.05;
    letter-spacing: 1px;
  }
  .back__name span { display: block; }
</style>
</head>
<body>
<main class="canvas">
  <section class="card card--front" aria-label="Business card front">
    <div class="front__band"></div>
    <div class="front__corner-block"></div>
    <div class="front__side-blue"></div>
    <div class="front__side-white"></div>
    <div class="front__ghost-name" aria-hidden="true">fenwick</div>
    <h1 class="front__name">paul K fenwick</h1>
    <p class="front__role">photographer</p>
    <dl class="front__contact">
      <div><dt>email •</dt><dd>lisamerrow@quillpost.com</dd></div>
      <div><dt>phone •</dt><dd>5183402917</dd></div>
    </dl>
  </section>

  <section class="card card--back" aria-label="Business card back">
    <div class="back__corner-block"></div>
    <div class="back__band"></div>
    <div class="back__band-thin"></div>
    <h2 class="back__name"><span>PAUL K</span><span>FENWICK</span></h2>
  </section>
</main>
</body>
</html>
```